依頼詳細
参考までにヨーロッパでのウォーカーのサイトです。
https://www.brenwick.com/our-products/exercisers/the-brenwick-halton/
https://www.marsett.co.uk/product-page/horsewalker/

残念ながらあまり多くの写真素材が無いので、うまくイラストや説明でフォローできると幸いです。
添付の写真はこちらが利用して良い素材になります。
記載項目
社名 株式会社ピーエスビーノルテ
連絡先 03-4827-1093
メール kurosu@psb-norte.com

代理店用のスペース
サイズ
A4
ページ数
両面
希望イメージ
シンプル 複雑
単色 カラフル
暗い 明るい
日常 高級
遊び心 厳粛
未来的 伝統的
女性的 男性的
希望する色
緑系、青系
納品ファイル
• イラストレーター形式 (.ai)
• フォトショップ形式 (.psd)
補足説明
写真がうまく掲載されていなかったので追記です

今回は素敵な提案をありがとうございます。
少ない商材の中わかりやすいイラストなど営業担当のものも喜んでいました。

今回はたくさんの提案ありがとうございます。
一つに選考するのに落選の皆様に心苦しい限りです。
また、別な機会に個別にお願いすることもあるかと思いますので今後ともよろしくお願いいたします

```html
<!DOCTYPE html>
<html lang="ja">
<head>
<meta charset="utf-8">
<title>馬用ウォーキングマシン TYPE A</title>
<link rel="stylesheet" href="https://fonts.googleapis.com/css2?family=Noto+Sans+JP:wght@400;500;700;900&family=Cinzel:wght@500&family=Orbitron:wght@800&display=swap">
<style>
:root{
  --green:#1f9a3c;
  --green-dark:#137a2c;
  --green-light:#e8f4ea;
  --yellow:#ffe14a;
  --ink:#2a2a2a;
  --white:#ffffff;
  --bg:#f6f8f5;
}
*{margin:0;padding:0;box-sizing:border-box}
html,body{width:848px;height:1200px;overflow:hidden;background:var(--white)}
body{font-family:"Noto Sans JP",sans-serif;color:var(--ink)}
.flyer{position:relative;width:848px;height:1200px;background:var(--bg);overflow:hidden}

.header{position:absolute;left:0;top:0;width:848px;height:150px;background:linear-gradient(180deg,var(--green) 0%,var(--green-dark) 100%);text-align:center}
.header-title{padding-top:14px;font-size:66px;font-weight:900;color:var(--white);letter-spacing:4px;line-height:1.1;text-shadow:0 3px 0 rgba(0,0,0,.18)}
.header-sub{margin-top:6px;font-family:"Cinzel",serif;font-size:22px;color:var(--white);letter-spacing:10px}

.type-name{position:absolute;left:150px;top:172px;width:470px;text-align:center;font-family:"Orbitron",sans-serif;font-size:58px;color:var(--green);letter-spacing:6px;line-height:1}
.type-rule{position:absolute;left:60px;top:168px;width:560px;height:3px;background:var(--green)}
.type-rule.bottom{top:236px}
.price{position:absolute;left:150px;top:244px;font-size:38px;font-weight:900;color:var(--green);display:flex;align-items:center;gap:16px}
.price svg{width:44px;height:30px}

.horse-art{position:absolute;left:580px;top:170px;width:230px;height:240px;border-radius:12px;background:linear-gradient(160deg,#a77b57 0%,#6e4428 100%)}

.spec-box{position:absolute;left:34px;top:300px;width:400px;height:130px;background:var(--green);border-radius:6px;padding:14px 22px;color:var(--white)}
.spec-roof{font-size:27px;font-weight:900;color:var(--yellow);letter-spacing:2px}
.spec-size{display:flex;margin-top:8px;font-size:26px;font-weight:700;line-height:1.35}
.spec-size .label{width:150px;color:var(--yellow)}

.photos{position:absolute;left:34px;top:442px;width:780px;height:270px;display:flex;gap:16px}
.photo{flex:1;border-radius:4px}
.photo.walker{background:linear-gradient(180deg,#b9c6cf 0%,#9aa79c 55%,#6f8a5a 100%)}
.photo.fence{background:linear-gradient(160deg,#cfd6d8 0%,#5b6468 55%,#3b4244 100%)}

.features{position:absolute;left:34px;top:728px;width:780px;height:170px;display:flex;gap:12px}
.feature-easy{width:220px;flex:none}
.pill{display:inline-block;background:var(--green);color:var(--yellow);font-size:22px;font-weight:900;padding:6px 22px;border-radius:30px}
.feature-easy p{margin-top:10px;font-size:14px;font-weight:500;line-height:1.7}
.badge{flex:none;width:124px;height:124px;border-radius:50%;background:var(--green);color:var(--white);display:flex;flex-direction:column;align-items:center;justify-content:center;text-align:center;font-size:16px;font-weight:900;line-height:1.3;margin-top:20px}
.badge svg{width:32px;height:32px;margin-bottom:6px}
.badge em{font-style:normal;color:var(--yellow)}

.option-table{flex:none;border-collapse:collapse;table-layout:fixed;width:264px;margin-left:auto;margin-top:12px;font-size:14px;background:var(--white)}
.option-table td{border:2px solid var(--green);padding:0 6px;height:36px;font-weight:700;white-space:nowrap;vertical-align:middle}
.option-table .c-dia{width:78px}
.option-table .c-head{width:58px}
.option-table .dia{background:var(--green-light);text-align:center}
.option-table .head{color:var(--green);text-align:center}
.option-table .add{color:var(--green-dark)}

.notes{position:absolute;left:34px;top:916px;width:780px;font-size:12.5px;line-height:1.7;color:#555}

.footer{position:absolute;left:0;top:990px;width:848px;height:210px;background:var(--white);border-top:6px solid var(--green)}
.brand{position:absolute;left:44px;top:68px;display:flex;align-items:center;gap:14px;font-size:40px;font-weight:700;color:var(--green);letter-spacing:2px}
.brand .dot{width:30px;height:30px;border-radius:50%;background:var(--green)}
.contact{position:absolute;right:44px;top:34px;text-align:right;color:var(--green-dark)}
.company{font-size:24px;font-weight:700}
.tel{margin-top:4px;font-size:44px;font-weight:900;display:flex;align-items:center;justify-content:flex-end;gap:10px}
.tel svg{width:36px;height:36px}
.mail{font-size:22px;font-weight:500}
.footer-band{position:absolute;left:0;bottom:0;width:848px;height:20px;background:var(--green)}
</style>
</head>
<body>
<div class="flyer">
  <header class="header">
    <h1 class="header-title">馬用ウォーキングマシン</h1>
    <div class="header-sub">HORSE WALKING MACHINE</div>
  </header>

  <div class="type-rule"></div>
  <div class="type-name">TYPE A</div>
  <div class="type-rule bottom"></div>
  <div class="price">標準価格
    <svg viewBox="0 0 44 30"><path d="M0 10h26V0l18 15-18 15V20H0z" fill="#1f9a3c"/></svg>
    120万円</div>

  <div class="horse-art" role="img" aria-label="鞍を付けた茶色の馬のイラスト"></div>

  <section class="spec-box">
    <div class="spec-roof">屋根なし　メッシュタイプ</div>
    <div class="spec-size"><span class="label">直径タイプ</span><span>16m ▶ 4頭用<br>18m ▶ 6頭用</span></div>
  </section>

  <div class="photos">
    <div class="photo walker" role="img" aria-label="屋外に設置された円形ウォーキングマシンの写真"></div>
    <div class="photo fence" role="img" aria-label="メッシュフェンスの接合部の写真"></div>
  </div>

  <section class="features">
    <div class="feature-easy">
      <span class="pill">設置が容易</span>
      <p>ウォーカー本体の基礎のみ、周囲のフェンスは直置き、もしくは地面への杭打ちのみ。</p>
    </div>
    <div class="badge">
      <svg viewBox="0 0 34 34" fill="none" stroke="#ffe14a" stroke-width="3" stroke-linecap="round"><path d="M3 12h20a5 5 0 1 0-5-5M3 19h26a5 5 0 1 1-5 5M3 26h12"/></svg>
      <span><em>強風</em>でも<br>煽られにくい</span>
    </div>
    <div class="badge">
      <svg viewBox="0 0 34 34"><circle cx="17" cy="17" r="15" fill="#ffe14a"/><path d="M11 9l6 8 6-8M17 17v10M12 19h10M12 23h10" stroke="#1f9a3c" stroke-width="3" fill="none"/></svg>
      <span><em>低コスト</em>で<br>導入可能</span>
    </div>
    <table class="option-table">
      <colgroup><col class="c-dia"><col class="c-head"><col></colgroup>
      <tr><td class="dia" rowspan="2">直径16m</td><td class="head">4頭用</td><td>▶ 標準価格</td></tr>
      <tr><td class="head">6頭用</td><td class="add">▶ +25万円</td></tr>
      <tr><td class="dia" rowspan="2">直径18m</td><td class="head">4頭用</td><td class="add">▶ +25万円</td></tr>
      <tr><td class="head">6頭用</td><td class="add">▶ +50万円</td></tr>
    </table>
  </section>

  <p class="notes">※表示価格は税別です。※価格は国内での本体価格です。※設置場所までの運送費は別途お見積もりになります。<br>※設置手配、設置費用はお客様のご負担となります。※ウォーカー部は TYPE B と同様のものです。</p>

  <footer class="footer">
    <div class="brand"><span class="dot"></span>P.S.B</div>
    <div class="contact">
      <div class="company">株式会社ピーエスビーノルテ</div>
      <div class="tel"><svg viewBox="0 0 24 24"><path d="M6.6 10.8a15 15 0 0 0 6.6 6.6l2.2-2.2a1 1 0 0 1 1-.25 11.4 11.4 0 0 0 3.6.6 1 1 0 0 1 1 1V20a1 1 0 0 1-1 1A17 17 0 0 1 3 4a1 1 0 0 1 1-1h3.5a1 1 0 0 1 1 1 11.4 11.4 0 0 0 .6 3.6 1 1 0 0 1-.25 1z" fill="#137a2c"/></svg>03-4827-1093</div>
      <div class="mail">E-mail：kurosu@psb-norte.com</div>
    </div>
    <div class="footer-band"></div>
  </footer>
</div>
</body>
</html>
```